New, modern business card for growing audiology practice

We need a new business card for our audiology practice. Our logo and website have recently changed (more modern) and we want our business cards to reflect this change.
We conduct hearing tests, perform earwax removals, and fit & dispense hearing aids to our patients. We are a family owned practice in which the owner is the one who works directly with the patient. I have attached logos in various formats to use, as well as two ideas I found on this website; as well as a scanned copy of our current logo. Good luck!

Industry/Entity Type

Business

Contact Information for Business Card

Company name: Maplow Hearing Center
Provider name: Peter Mulvoy, Au.D. F/ISN
Phone number: (555) 318-6042
Address: 87 W. Linden Ave. Wrenfield, OH 43990
email: maplowhearing@postvale.net
website: maplowhearing.com

Colors
000000
aaaaaa
dbdbdb
cacaca
9bcb3c
afd23c
cadf82
b1b1b1

Requirements
Must have
• My card must include information in the "details" section. In the attached images, I found a few that I liked and I would like to model after - "brisk tumblin'" and "Sound Wellness Center".
• Must be horizontal.
• Must include logos provided. I uploaded them in various file formats and various ways.
• Must match logo font, if possible, if not, please get as close as you can.
Nice to have
• I really like the idea of having a color on one side with just the logo and company name and the contact information and provider name on the other side. I also really like the idea of having the main color dominating on the logo/company side with accent of that same color on the contact side of the card.
Should not have
• Must not be vertical.

```html
<!DOCTYPE html>
<html lang="en">
<head>
<meta charset="utf-8">
<title>Maplow Hearing Center – Business Card</title>
<link rel="stylesheet" href="https://fonts.googleapis.com/css2?family=Cabin:wght@400&family=Saira+Semi+Condensed:wght@600&family=Roboto:wght@400&display=swap">
<style>
  :root {
    --backdrop: #bdbdbd;
    --brand-green: #5a9234;
    --brand-green-dark: #4f852c;
    --accent-green: #4f8f2a;
    --card-white: #f2f2f2;
    --card-white-edge: #e4e4e4;
    --ink: #111111;
    --ink-soft: #1c1c1c;
    --white: #ffffff;
  }
  * { margin: 0; padding: 0; box-sizing: border-box; }
  html, body {
    width: 1200px; height: 576px; overflow: hidden;
    background: var(--backdrop);
  }
  .canvas { position: relative; width: 1200px; height: 576px; }

  .card {
    position: absolute; top: 138px;
    width: 485px; height: 294px;
    border-radius: 12px;
    overflow: hidden;
  }
  .card--front {
    left: 82px;
    background: linear-gradient(180deg, var(--brand-green) 0%, var(--brand-green-dark) 100%);
  }
  .card--back {
    left: 602px;
    background: linear-gradient(180deg, var(--card-white) 0%, var(--card-white-edge) 100%);
  }

  .wordmark {
    font-family: "Cabin", "Gill Sans", sans-serif;
    font-weight: 400;
    text-transform: uppercase;
    line-height: 1;
  }
  .card--front .wordmark {
    position: absolute; left: 0; right: 0; top: 112px;
    text-align: center;
    color: var(--white);
  }
  .wordmark__line--main { display: block; font-size: 36px; letter-spacing: 0.5px; }
  .wordmark__line--sub { display: block; font-size: 18px; margin-top: 6px; letter-spacing: 0.3px; }

  .provider {
    position: absolute; left: 30px; top: 30px;
  }
  .provider__name {
    font-family: "Saira Semi Condensed", "Arial Narrow", sans-serif;
    font-weight: 600; font-size: 19px;
    color: var(--accent-green);
  }
  .provider__role {
    font-family: "Roboto", Arial, sans-serif;
    font-size: 11.5px; color: var(--ink-soft);
    margin-top: 6px;
  }

  .contact {
    position: absolute; left: 30px; top: 174px;
    list-style: none;
    font-family: "Roboto", Arial, sans-serif;
    font-size: 12.5px; line-height: 16.5px;
    color: var(--ink-soft);
  }
  .contact__item { display: flex; align-items: flex-start; }
  .contact__icon { width: 10px; height: 10px; margin-top: 3px; margin-right: 10px; flex: none; fill: var(--accent-green); }
  .contact__text--indent { padding-left: 20px; }

  .card--back .wordmark {
    position: absolute; right: 36px; top: 214px;
    text-align: left;
    color: var(--ink);
  }
  .card--back .wordmark__line--main { font-size: 26px; }
  .card--back .wordmark__line--sub { font-size: 14px; margin-top: 3px; }
</style>
</head>
<body>
<div class="canvas">

  <section class="card card--front" aria-label="Card front">
    <h1 class="wordmark">
      <span class="wordmark__line--main">Maplow</span>
      <span class="wordmark__line--sub">Hearing Center</span>
    </h1>
  </section>

  <section class="card card--back" aria-label="Card back">
    <div class="provider">
      <p class="provider__name">Peter Mulvoy, Au.D. F/ISN</p>
      <p class="provider__role">Owner - Audiologist</p>
    </div>

    <ul class="contact">
      <li class="contact__item">
        <svg class="contact__icon" viewBox="0 0 10 10" aria-hidden="true"><path d="M5 0a3.6 3.6 0 0 0-3.6 3.6C1.4 6.3 5 10 5 10s3.6-3.7 3.6-6.4A3.6 3.6 0 0 0 5 0zm0 5a1.4 1.4 0 1 1 0-2.8A1.4 1.4 0 0 1 5 5z"/></svg>
        <span>87 W. Linden Ave.</span>
      </li>
      <li class="contact__item contact__text--indent">Wrenfield, OH 43990</li>
      <li class="contact__item">
        <svg class="contact__icon" viewBox="0 0 10 10" aria-hidden="true"><path d="M0 3.2C0 2 1.5 1 5 1s5 1 5 2.2V4H7V3H3v1H0z"/><path d="M1.5 5h7l.7 4H.8z"/></svg>
        <span>(555) 318-6042</span>
      </li>
      <li class="contact__item">
        <svg class="contact__icon" viewBox="0 0 10 10" aria-hidden="true"><path d="M0 2h10v.6L5 5.8 0 2.6z"/><path d="M0 3.6l5 3.2 5-3.2V8H0z"/></svg>
        <span>maplowhearing@postvale.net</span>
      </li>
      <li class="contact__item">
        <svg class="contact__icon" viewBox="0 0 10 10" aria-hidden="true"><circle cx="5" cy="5" r="4.3" fill="none" stroke="var(--accent-green)" stroke-width="1"/><ellipse cx="5" cy="5" rx="1.8" ry="4.3" fill="none" stroke="var(--accent-green)" stroke-width="0.9"/><path d="M0.7 5h8.6" stroke="var(--accent-green)" stroke-width="0.9"/></svg>
        <span>www.maplowhearing.com</span>
      </li>
    </ul>

    <div class="wordmark">
      <span class="wordmark__line--main">Maplow</span>
      <span class="wordmark__line--sub">Hearing Center</span>
    </div>
  </section>

</div>
</body>
</html>
```